Larkfield Rowhomes - Billboard design for our newly renovated townhome community

We have a 5' wide x 4' tall billboard at the entrance to our apartment community, that needs to have the acrylic insert replaced. It is a 2 sided sign, and we are planning to use the same image on both sides. We are called Larkfield Rowhomes, and have 48 townhomes that are all 2 bedroom, 1 1/2 bath. A few things we would like to get across on the signage: "Newly Renovated" "2 bed 1 1/2 bath" "Full size W/D in every home" " New Appliances" I've included our parent company's logo - this is the only image I could think of, but it might not be worth having it on the sign. We are in Colorado, so mountain theme could be nice and also sunshine/sun since we are called "Larkfield"

Industry/Entity Type

Apartment

Font styles to use
Sans Serif

Requirements
Must have
• Newly Renovated
2 bed 1 1/2 bath
Full size W/D in every home
Virtual Tours available
www.brambletonhomesco.example
855 - 413 - 9286
Nice to have
• We are located in Colorado - possibly mountain theme? Since our community is called "Larkfield Rowhomes" - anything bright with Sun / Sunshine might look really nice as well.

```html
<!DOCTYPE html>
<html lang="en">
<head>
<meta charset="utf-8">
<title>Larkfield Rowhomes – Entrance Billboard</title>
<link rel="stylesheet" href="https://fonts.googleapis.com/css2?family=Bebas+Neue&display=swap">
<style>
  :root {
    --stage: #1b1b1d;
    --sky-top: #1f4f8f;
    --sky-mid: #3b7fc2;
    --rock-light: #c98a5a;
    --rock-deep: #9c4a26;
    --ground: #b5532b;
    --title-red: #e51f25;
    --accent-yellow: #f7ec1a;
    --band-black: #0a0a0a;
    --band-text: #ffffff;
  }
  * { box-sizing: border-box; margin: 0; padding: 0; }
  html, body {
    width: 1200px; height: 479px; overflow: hidden;
    background: var(--stage);
  }
  .stage {
    width: 1200px; height: 479px;
    display: flex; align-items: center; justify-content: center;
  }
  .billboard {
    position: relative;
    width: 600px; height: 479px;
    overflow: hidden;
    font-family: "Bebas Neue", "Oswald", sans-serif;
  }
  .landscape {
    position: absolute; left: 0; top: 0;
    width: 600px; height: 433px;
    background:
      linear-gradient(180deg,
        var(--sky-top) 0%,
        var(--sky-mid) 45%,
        var(--rock-light) 58%,
        var(--rock-deep) 78%,
        var(--ground) 100%);
  }
  .title {
    position: absolute; left: 0; right: 0; top: 6px;
    text-align: center;
    color: var(--title-red);
    -webkit-text-stroke: 1.5px var(--accent-yellow);
    paint-order: stroke fill;
    line-height: 0.86;
  }
  .title-line { display: block; font-size: 106px; letter-spacing: 1px; }
  .title-line--second { font-size: 104px; }
  .features {
    position: absolute; left: 0; right: 0; top: 184px;
    text-align: center;
    color: var(--accent-yellow);
    font-size: 24px;
    letter-spacing: 0.3px;
    white-space: nowrap;
  }
  .features .divider { margin: 0 8px; }
  .tour-badge {
    position: absolute; left: 258px; top: 216px;
    width: 100px; height: 98px;
  }
  .tour-badge svg { position: absolute; inset: 0; }
  .tour-badge-text {
    position: absolute; inset: 0;
    display: flex; flex-direction: column; align-items: center; justify-content: center;
    color: var(--accent-yellow);
    line-height: 0.9;
    transform: rotate(-4deg);
  }
  .tour-badge-text .strong { font-size: 22px; }
  .tour-badge-text .light { font-size: 17px; }
  .contact-band {
    position: absolute; left: 0; bottom: 0;
    width: 600px; height: 46px;
    background: var(--band-black);
    color: var(--band-text);
    display: flex; align-items: center; justify-content: center;
    font-size: 31px; letter-spacing: 0.4px;
    white-space: nowrap;
  }
  .contact-band .divider { margin: 0 12px; }
</style>
</head>
<body>
  <main class="stage">
    <section class="billboard">
      <div class="landscape" role="img" aria-label="Photograph of red sandstone rock formations under a clear blue sky"></div>

      <h1 class="title">
        <span class="title-line">Larkfield</span>
        <span class="title-line title-line--second">Rowhomes</span>
      </h1>

      <p class="features">
        Newly Renovated<span class="divider">|</span>2 Bed 1½ Bath<span class="divider">|</span>Full Size W/D in Every Home
      </p>

      <div class="tour-badge">
        <svg viewBox="0 0 100 98" aria-hidden="true">
          <path d="M8 10 Q6 3 13 3 L90 6 Q97 7 96 14 L90 70 Q89 76 83 78 L30 94 Q23 96 21 89 Z"
                fill="var(--title-red)" stroke="var(--accent-yellow)" stroke-width="3" stroke-linejoin="round"/>
        </svg>
        <div class="tour-badge-text">
          <span class="strong">Virtual</span>
          <span class="strong">Tours</span>
          <span class="light">Available</span>
        </div>
      </div>

      <footer class="contact-band">
        <span class="contact-web">www.brambletonhomesco.example</span>
        <span class="divider">|</span>
        <span class="contact-phone">855 - 413 - 9286</span>
      </footer>
    </section>
  </main>
</body>
</html>
```